Handout postcard for tradeshow

Please create a 2-sided handout postcard for use at a tradeshow. Card should be 4.25" x 5.5"

While postcard sized, a postcard with a place for an address/stamp is not wanted. We want a small handout for a tradeshow for people to take home with them.

The first side should emphasize cost savings.
The second side should emphasize environmental benefits.

The card's design doesn't need to match, but should be in line with the included poster design which will also be used at the tradeshow.

Possible graphics to include are listed below as well as the poster it should emulate.

```html
<!DOCTYPE html>
<html lang="en">
<head>
<meta charset="utf-8">
<title>RouteLane Tradeshow Handout</title>
<link rel="stylesheet" href="https://fonts.googleapis.com/css2?family=Montserrat:wght@300;400;800&family=Source+Sans+3:wght@300;400;600;700&display=swap">
<style>
  :root{
    --stage:#666666;
    --blue:#29a6df;
    --sky:#3ec2ef;
    --green:#3db14a;
    --slate:#4b4b4b;
    --ink:#5b5b5b;
    --white:#ffffff;
  }
  *{margin:0;padding:0;box-sizing:border-box}
  html,body{width:796px;height:1200px;overflow:hidden;background:var(--stage)}
  body{position:relative;font-family:"Source Sans 3",sans-serif;color:var(--white)}
  .card{position:absolute;left:63px;width:657px;height:507px;overflow:hidden;background:var(--white)}
  .card--front{top:66px}
  .card--back{top:631px}
  .band{position:absolute;left:0;width:100%}
  .layer{position:absolute;inset:0;width:657px;height:507px}
  .txt{position:absolute;z-index:3}

  /* front */
  .brand{font-family:"Montserrat",sans-serif;font-weight:800;letter-spacing:-1px;line-height:1;display:flex;align-items:center;gap:7px;white-space:nowrap}
  .brand__dot{flex:none;border-radius:50%;background:var(--blue)}
  .brand--front{left:41px;top:34px;font-size:36px;color:var(--ink)}
  .brand--front .brand__dot{width:38px;height:38px}
  .kicker{font-family:"Montserrat",sans-serif;font-weight:300;font-size:19px;line-height:1}
  .headline{font-family:"Montserrat",sans-serif;font-weight:800;font-size:29px;line-height:30px;letter-spacing:.2px}
  .mission{left:24px;top:208px;width:290px;font-size:13.2px;line-height:16px;font-weight:400}
  .cost-lead{left:24px;top:308px;font-size:12.5px;font-weight:300}
  .cost-big{left:24px;top:322px;font-size:27px;font-weight:700;letter-spacing:.2px}
  .using{left:23px;top:370px;font-size:15.5px;font-weight:600}
  .stat{position:absolute;top:399px;height:63px;border:1.5px dotted rgba(255,255,255,.9);text-align:center;z-index:3}
  .stat__num{font-family:"Montserrat",sans-serif;font-weight:800;font-size:25px;line-height:1;margin-top:8px}
  .stat__label{font-size:14px;font-weight:600;margin-top:4px}
  .stat--carbon{left:23px;width:156px}
  .stat--trucks{left:201px;width:168px}
  .contact{position:absolute;display:flex;align-items:center;gap:8px;font-size:12.5px;letter-spacing:1.6px;z-index:3}
  .contact svg{width:18px;height:18px}

  /* back */
  .benefit{position:absolute;left:24px;z-index:3}
  .benefit__icon{position:absolute;left:0;top:0;width:34px;height:34px;border-radius:6px;background:var(--white);display:flex;align-items:center;justify-content:center}
  .benefit__title{margin-left:43px;padding-top:9px;font-size:12.8px;font-weight:700;letter-spacing:-.1px;white-space:nowrap}
  .benefit__body{margin-left:43px;margin-top:6px;font-size:9.4px;line-height:12px;font-weight:400}
  .brand--back{left:46px;top:422px;font-size:29px;color:var(--white)}
  .brand--back .brand__dot{width:30px;height:30px;background:var(--white)}
</style>
</head>
<body>

<section class="card card--front" aria-label="Front of handout">
  <div class="band" style="top:102px;height:196px;background:var(--blue)"></div>
  <div class="band" style="top:298px;height:65px;background:var(--sky)"></div>
  <div class="band" style="top:363px;height:111px;background:var(--green)"></div>
  <div class="band" style="top:474px;height:33px;background:var(--slate)"></div>

  <svg class="layer" style="z-index:2" viewBox="0 0 657 507" aria-hidden="true">
    <polygon points="353,0 657,0 657,507 426,507 296,203" fill="var(--white)"/>
  </svg>
  <svg class="layer" style="z-index:2" viewBox="0 0 657 507" role="img" aria-label="Photo of a city skyline at dusk above a highway with light trails">
    <defs>
      <linearGradient id="dusk1" x1="0" y1="0" x2="0" y2="1">
        <stop offset="0" stop-color="#3f5a7c"/>
        <stop offset=".35" stop-color="#6f7f95"/>
        <stop offset=".55" stop-color="#2f3540"/>
        <stop offset=".8" stop-color="#3a3a44"/>
        <stop offset="1" stop-color="#6b3a36"/>
      </linearGradient>
    </defs>
    <polygon points="373,0 657,0 657,507 464,507 305,203" fill="url(#dusk1)"/>
  </svg>

  <div class="txt brand brand--front"><span class="brand__dot"></span>RouteLane</div>
  <div class="txt kicker" style="left:26px;top:119px">Join the</div>
  <div class="txt headline" style="left:26px;top:140px">GREEN PARCEL<br>MOVEMENT</div>
  <p class="txt mission">Our mission is to take the waste out of shipping. Every carrier drives every street in the US daily duplicating each others’ routes. We help consolidate routes across carriers using our real-time bidding system for parcels.</p>
  <div class="txt cost-lead">RouteLane Cuts the Waste out of Parcel Shipping &amp;</div>
  <div class="txt cost-big">Reduces Costs by 10-50%</div>
  <div class="txt using">SEND YOUR PARCELS USING</div>
  <div class="stat stat--carbon"><div class="stat__num">40% Less</div><div class="stat__label">CARBON EMISSIONS</div></div>
  <div class="stat stat--trucks"><div class="stat__num">25% Less</div><div class="stat__label">TRUCKS ON THE ROAD</div></div>

  <div class="contact" style="left:38px;top:481px">
    <svg viewBox="0 0 20 20"><circle cx="10" cy="10" r="10" fill="var(--green)"/><circle cx="10" cy="10" r="6" fill="none" stroke="#fff" stroke-width="1.3"/><ellipse cx="10" cy="10" rx="2.6" ry="6" fill="none" stroke="#fff" stroke-width="1.1"/><line x1="4" y1="10" x2="16" y2="10" stroke="#fff" stroke-width="1.1"/></svg>
    www.routelane.com
  </div>
  <div class="contact" style="left:249px;top:481px">
    <svg viewBox="0 0 20 20"><circle cx="10" cy="10" r="10" fill="var(--green)"/><rect x="5" y="6.5" width="10" height="7" rx="1" fill="#fff"/><polyline points="5.5,7 10,10.8 14.5,7" fill="none" stroke="var(--green)" stroke-width="1.1"/></svg>
    info@routelane.com
  </div>
</section>

<section class="card card--back" aria-label="Back of handout">
  <div class="band" style="top:0;height:108px;background:var(--blue)"></div>
  <div class="band" style="top:108px;height:292px;background:var(--green)"></div>
  <div class="band" style="top:400px;height:71px;background:var(--sky)"></div>
  <div class="band" style="top:471px;height:36px;background:var(--slate)"></div>

  <svg class="layer" style="z-index:2" viewBox="0 0 657 507" aria-hidden="true">
    <polygon points="320,0 657,0 657,507 230,507 388,201" fill="var(--white)"/>
  </svg>
  <svg class="layer" style="z-index:2" viewBox="0 0 657 507" role="img" aria-label="Photo of downtown towers at dusk with curving highway light trails">
    <defs>
      <linearGradient id="dusk2" x1="0" y1="0" x2="0" y2="1">
        <stop offset="0" stop-color="#5c6e86"/>
        <stop offset=".4" stop-color="#7d8594"/>
        <stop offset=".6" stop-color="#2c323b"/>
        <stop offset=".85" stop-color="#353842"/>
        <stop offset="1" stop-color="#6a4a3c"/>
      </linearGradient>
    </defs>
    <polygon points="340,0 657,0 657,507 269,507 397,201" fill="url(#dusk2)"/>
  </svg>

  <div class="txt kicker" style="left:27px;top:17px">Cutting eCommerce</div>
  <div class="txt headline" style="left:27px;top:39px">SHIPPING COSTS<br>AND EMISSIONS</div>

  <div class="benefit" style="top:119px">
    <div class="benefit__icon"><svg width="22" height="22" viewBox="0 0 22 22"><circle cx="11" cy="8" r="5" fill="none" stroke="var(--green)" stroke-width="1.2"/><text x="11" y="11" font-size="7" text-anchor="middle" fill="var(--green)" font-family="sans-serif">$</text><path d="M3 17 q4 -3 8 0 h6" fill="none" stroke="var(--green)" stroke-width="1.2"/></svg></div>
    <div class="benefit__title">EASY, RISK-FREE SAVINGS</div>
    <p class="benefit__body" style="width:292px">Put your shipments up for bid via RouteLane’s simple API integration and receive a response in less than a second. You only use our real-time rates when we beat your contracted rate. No downside. No commitments necessary</p>
  </div>
  <div class="benefit" style="top:210px">
    <div class="benefit__icon"><svg width="22" height="22" viewBox="0 0 22 22"><rect x="4" y="4" width="7" height="7" fill="none" stroke="var(--green)" stroke-width="1.2"/><rect x="11" y="4" width="7" height="7" fill="none" stroke="var(--green)" stroke-width="1.2"/><rect x="7.5" y="11" width="7" height="7" fill="none" stroke="var(--green)" stroke-width="1.2"/></svg></div>
    <div class="benefit__title">A GREEN PARCEL IS A CHEAP PARCEL</div>
    <p class="benefit__body" style="width:250px">When a carrier is already serving an address, they can underbid other carriers for the next package, since they have already paid for that stop. This lowers shipping costs, reduces the number of duplicate stops, and cuts carbon emissions.</p>
  </div>
  <div class="benefit" style="top:307px">
    <div class="benefit__icon"><svg width="24" height="22" viewBox="0 0 24 22"><rect x="2" y="6" width="12" height="9" fill="none" stroke="var(--green)" stroke-width="1.2"/><path d="M14 9 h4 l3 3 v3 h-7z" fill="none" stroke="var(--green)" stroke-width="1.2"/><circle cx="6" cy="16.5" r="1.8" fill="#fff" stroke="var(--green)" stroke-width="1.2"/><circle cx="17" cy="16.5" r="1.8" fill="#fff" stroke="var(--green)" stroke-width="1.2"/><polyline points="5,10 7,12 11,8" fill="none" stroke="var(--green)" stroke-width="1.2"/></svg></div>
    <div class="benefit__title">QUICKLY VALIDATE SAVINGS</div>
    <p class="benefit__body" style="width:200px">Connect with us to run a back-test on your shipping data, and see exactly how much money you would've saved on each parcel if you'd used RouteLane for the past 3 months</p>
  </div>

  <div class="txt brand brand--back"><span class="brand__dot"></span>RouteLane</div>
  <div class="contact" style="left:46px;top:480px">
    <svg viewBox="0 0 20 20"><circle cx="10" cy="10" r="10" fill="var(--green)"/><circle cx="10" cy="10" r="6" fill="none" stroke="#fff" stroke-width="1.3"/><ellipse cx="10" cy="10" rx="2.6" ry="6" fill="none" stroke="#fff" stroke-width="1.1"/><line x1="4" y1="10" x2="16" y2="10" stroke="#fff" stroke-width="1.1"/></svg>
    www.routelane.com
  </div>
</section>

</body>
</html>
```